Hotel representation company, Veridane, needs a Marketing sheet

Veridane representation needs a company portfolio listing - one sheet - marketing piece featuring each property in the portfolio. Veridane is a hotel representation company selling to the North America travel trade.
Showcasing the world’s distinct and diverse destinations, Veridane represents a global collection of exceptional luxury properties - each united and underpinned by immersive experiences that connect people to place. Veridane is a trusted resource and representation for experiential luxury and the travel trade at large, providing enhanced exposure and training throughout North America and beyond. Founded on curiosity, exploration and the desire to travel deeper, the Veridane experience unites the polarity of the world’s far-flung destinations through a rich tapestry of connections designed to inspire, intrigue and immerse.

Target Market(s)

Premium travel industry; those seeking experiential luxury, willing to travel off grid

Industry/Entity Type

Travel Industry

Font styles to use
Other font styles liked:
• Garamond, Bell MT, Century Gothic, Bookman Old Style

Colors
0054AA
0677BA
7BADD7
CADEEF
E8F1F8
0094D4
00A9DD
6FCCEA
C7EBF8
E9F6FB
00AB8E
00BBA5
67D7C9
C6EFE9
E9F9F6

Requirements
Must have
• Veridane logo, My contact information, a listing of portfolio - website and optional logo
Nice to have
• Images
Should not have
• Text about the property as too detailed

```html
<!DOCTYPE html>
<html lang="en">
<head>
<meta charset="utf-8">
<title>Veridane – Experiential Luxury Portfolio Sheet</title>
<link rel="stylesheet" href="https://fonts.googleapis.com/css2?family=EB+Garamond:wght@400;500&family=Didact+Gothic&display=swap">
<style>
:root{
  --board:#0b2fa3;
  --white:#ffffff;
  --brand:#0054aa;
  --brand-mid:#0677ba;
  --ink:#3c3c3c;
  --ink-soft:#6e6e6e;
  --rule:#d9dde3;
  --teal:#3fa3ac;
  --maroon:#8a3a3a;
  --tint-sand:#f4eee7;
  --tint-mist:#f6f6f4;
  --tint-sage:#e7ece8;
  --tint-butter:#fbf2d9;
  --tint-aqua:#d6eef1;
  --tint-rose:#ecdcdc;
  --tint-slate:#d8dfe4;
  --serif:"EB Garamond", Garamond, serif;
  --sans:"Didact Gothic", "Century Gothic", sans-serif;
}
*{box-sizing:border-box;margin:0;padding:0}
html,body{width:1200px;height:720px;overflow:hidden}
body{background:var(--board);font-family:var(--sans);color:var(--ink);position:relative}

.pitch{position:absolute;left:52px;top:186px;color:var(--white)}
.pitch__lines{font-family:var(--serif);font-weight:400;font-size:35px;line-height:43px}
.pitch__spec{font-family:var(--sans);font-size:19px;line-height:23px;margin-top:34px;width:160px}

.sheet{position:absolute;width:431px;height:323px;background:var(--white);display:grid;
  grid-template-columns:83px repeat(3,1fr);grid-template-rows:1fr 1fr;overflow:hidden}
.sheet--front-tinted{left:265px;top:28px}
.sheet--front-plain{left:720px;top:28px}
.sheet--back-tinted{left:265px;top:368px}
.sheet--back-plain{left:720px;top:368px}

.identity{grid-row:1 / span 2;position:relative;padding:20px 8px 0 17px}
.sheet--front-plain .identity,.sheet--back-plain .identity{border-right:1px solid var(--brand)}
.identity__mark{display:flex;align-items:center;gap:3px;font-family:var(--serif);color:var(--brand);
  font-size:9.5px;letter-spacing:.3px;font-variant:small-caps}
.identity__mark i{width:5px;height:5px;border-radius:50%;background:var(--brand);display:block}
.identity__title{position:absolute;left:12px;top:82px;height:137px;display:flex;align-items:flex-end;gap:4px}
.tagline{writing-mode:vertical-rl;transform:rotate(180deg);font-family:var(--serif);color:var(--brand);
  font-size:19px;line-height:19px;white-space:nowrap;text-align:left}
.identity__title--large{top:52px;height:165px}
.identity__title--large .tagline{font-size:22px;line-height:21px}
.portfolio{font-size:6px;line-height:7px;color:var(--ink);padding-bottom:2px}
.portfolio ul{list-style:none;color:var(--brand-mid);font-size:5px;line-height:6px;margin-top:4px}
.contact{position:absolute;left:17px;top:265px;font-size:5.2px;line-height:9px;color:var(--ink)}
.contact__name{font-weight:700;font-size:7px;letter-spacing:.2px}
.contact__phone{color:var(--brand);font-family:var(--serif);font-size:7px}

.listing{padding:19px 6px 4px 6px;display:flex;flex-direction:column;min-width:0}
.sheet--front-plain .listing,.sheet--back-plain .listing{border-left:1px solid var(--rule);border-bottom:1px solid var(--rule)}
.listing__label{font-size:3.6px;line-height:5.4px;color:var(--ink);text-transform:uppercase;letter-spacing:.2px}
.listing__label b{font-weight:700}
.listing__label span{color:var(--ink-soft)}
.sheet--front-plain .listing__label,.sheet--back-plain .listing__label{color:var(--brand)}
.listing__group{font-size:3.6px;color:var(--ink-soft);line-height:5px}
.listing__headline{font-family:var(--serif);font-weight:400;font-size:8px;line-height:10px;color:var(--ink-soft);margin-top:5px;height:21px}
.listing__headline--teal{color:var(--teal)}
.listing__headline--maroon{color:var(--maroon)}
.listing__photos{height:62px;display:grid;grid-template-columns:1fr 1fr;grid-template-rows:1fr 1fr;gap:1.5px;margin-top:2px;position:relative}
.listing__photos--wide{grid-template-columns:1.7fr 1fr}
.tile{display:block}
.tile--tall{grid-row:span 2}
.tile-tag{position:absolute;color:var(--white);font-size:3.6px;line-height:5px;left:3px}
.tile-tag--top{top:3px}
.tile-tag--low{bottom:3px}
.tile-tag--right{left:auto;right:3px;bottom:3px;text-align:right}
.t-sea{background:linear-gradient(160deg,#5fc4d0,#1d8aa3)}
.t-reef{background:linear-gradient(135deg,#7fd6d8,#e4d7b6)}
.t-food{background:linear-gradient(135deg,#5c4a2e,#b3623a)}
.t-dusk{background:linear-gradient(180deg,#9aa6b3,#4a5f6c)}
.t-plain{background:linear-gradient(180deg,#c9b48a,#8a6d3d)}
.t-lake{background:linear-gradient(180deg,#8fb5cf,#2f5d7a)}
.t-forest{background:linear-gradient(160deg,#4c6a45,#1f3322)}
.t-river{background:linear-gradient(180deg,#b8c7cf,#5e7a86)}
.t-stone{background:linear-gradient(160deg,#8f8a7e,#4d4a44)}
.t-mount{background:linear-gradient(180deg,#a9c3dc,#6d7f6c)}
.t-horse{background:linear-gradient(180deg,#b7c8d8,#8a7453)}
.t-hill{background:linear-gradient(160deg,#7c8f57,#3e4f2d)}
.t-night{background:linear-gradient(160deg,#2f3a4e,#12182a)}
.t-beach{background:linear-gradient(160deg,#f1f1ec,#48b6c6)}
.t-red{background:linear-gradient(160deg,#b3442d,#5a2a1e)}
.t-sunset{background:linear-gradient(180deg,#d6936a,#7a3b28)}
.t-room{background:linear-gradient(160deg,#d8d2c6,#8b7f6c)}
.t-vine{background:linear-gradient(180deg,#98b56a,#4c6a2c)}
.t-pool{background:linear-gradient(160deg,#2d7bb4,#143a63)}
.listing__body{font-size:3.1px;line-height:4.4px;color:var(--ink-soft);margin-top:4px;height:22px;overflow:hidden}
.listing__foot{margin-top:auto;display:flex;justify-content:space-between;align-items:center;font-size:3.1px;color:var(--ink-soft)}
.listing__brand{display:flex;align-items:center;gap:2px;font-family:var(--serif);font-size:4.6px;color:var(--ink-soft);text-transform:uppercase;letter-spacing:.3px}
.listing__brand i{width:4px;height:4px;border-radius:50%;background:var(--ink-soft);display:block}

.sheet--front-tinted .listing--sand{background:var(--tint-sand)}
.sheet--front-tinted .listing--mist{background:var(--tint-mist)}
.sheet--front-tinted .listing--sage{background:var(--tint-sage)}
.sheet--front-tinted .listing--butter{background:var(--tint-butter)}
.sheet--back-tinted .listing--aqua{background:var(--tint-aqua)}
.sheet--back-tinted .listing--rose{background:var(--tint-rose)}
.sheet--back-tinted .listing--slate{background:var(--tint-slate)}
</style>
</head>
<body>

<section class="pitch">
  <h1 class="pitch__lines">Created in<br>Slidecraft<br>Easy to edit<br>Minimal<br>design</h1>
  <p class="pitch__spec">8.5”x11” double sided brochure, can be printed and shared digitally</p>
</section>

<!-- Front, tinted -->
<section class="sheet sheet--front-tinted">
  <aside class="identity">
    <div class="identity__mark"><i></i>Veridane</div>
    <div class="identity__title">
      <h2 class="tagline">Experiential<br>Luxury</h2>
      <div class="portfolio">The<br>Veridane<br>portfolio<ul><li>Australia</li><li>New Zealand</li><li>Chile</li><li>Canada</li></ul></div>
    </div>
    <address class="contact"><div class="contact__name">Marla Quinn</div>Marla@Veridane.net<br><span class="contact__phone">555-210-4478</span><br>www.veridane.net</address>
  </aside>

  <article class="listing listing--sand">
    <p class="listing__label"><b>Coralis</b><br><span>Hamilton Island, Queensland</span></p>
    <h3 class="listing__headline">Exquisite Great Barrier Reef experience</h3>
    <div class="listing__photos" role="img" aria-label="Island resort, heart-shaped reef from above and seafood platter">
      <span class="tile t-dusk"></span><span class="tile tile--tall t-food"></span><span class="tile t-reef"></span>
      <span class="tile-tag tile-tag--low">16+ years<br>60 Pavilions</span>
    </div>
    <p class="listing__body">Unsurpassed beauty, privacy and intuitive service. Stay three nights to explore Hamilton Island and the Great Barrier Reef.</p>
    <footer class="listing__foot"><span>www.coralis.com.au</span><span class="listing__brand">Coralis</span></footer>
  </article>

  <article class="listing listing--mist">
    <p class="listing__label"><b>Chile: Vientos Hotels:<br>Atacama, Chiloé &amp; Patagonia</b></p>
    <p class="listing__group">Harrow Lodges</p>
    <h3 class="listing__headline">Family run and welcoming to children 10+ years</h3>
    <div class="listing__photos listing__photos--wide" role="img" aria-label="Desert lodge with horses, lake boat and mountain views">
      <span class="tile t-plain" style="grid-column:span 2"></span><span class="tile t-lake"></span><span class="tile t-river"></span>
      <span class="tile-tag tile-tag--top">10+ years<br>28-40 Suites</span>
    </div>
    <p class="listing__body">Vientos Hotels are a collection of small boutique hotels across Chile, each with a tangible energy and a true connection to place.</p>
    <footer class="listing__foot"><span>info@vientoshotels.com</span><span class="listing__brand"><i></i>Vientos</span></footer>
  </article>

  <article class="listing listing--sage">
    <p class="listing__label"><b>Canada: Cedarline Wilderness Lodge,<br>Vancouver Island, British Columbia</b><br><span>Harrow Lodges</span></p>
    <h3 class="listing__headline">A true Canadian Safari experience</h3>
    <div class="listing__photos" role="img" aria-label="Riders crossing a river, forest canopy tents and wildlife">
      <span class="tile t-mount"></span><span class="tile t-river"></span><span class="tile t-forest"></span><span class="tile t-hill"></span>
      <span class="tile-tag tile-tag--top">6+ years<br>25 Tents</span>
    </div>
    <p class="listing__body">Cedarline Wilderness Lodge, set in remote Vancouver Island, delivers wild luxury under canvas.</p>
    <footer class="listing__foot"><span>www.cedarlinewilderness.com</span><span class="listing__brand">Cedarline</span></footer>
  </article>

  <article class="listing">
    <p class="listing__label"><b>New Zealand<br>Taurapa Lodge, Taupo, North Island</b><br><span>Harrow Lodges</span></p>
    <h3 class="listing__headline">New Zealand’s fly-fishing premium lodges</h3>
    <div class="listing__photos listing__photos--wide" role="img" aria-label="Stone lodge on manicured lawn beside a river">
      <span class="tile t-stone"></span><span class="tile t-river"></span><span class="tile t-hill"></span><span class="tile t-forest"></span>
      <span class="tile-tag tile-tag--right">22 Suites/<br>Residences</span>
    </div>
    <p class="listing__body">Taurapa Lodge delivers warm hospitality and views of the Waikato River. Fly fishing, rafting, golf, spa and heli excursions. A 3 night stay is ideal.</p>
    <footer class="listing__foot"><span>www.taurapalodge.com</span><span class="listing__brand">Taurapa Lodge</span></footer>
  </article>

  <article class="listing listing--butter">
    <p class="listing__label"><b>The Kestrel Group</b><br><span>North &amp; South Islands</span></p>
    <h3 class="listing__headline">Artistic architecture to complement the environments</h3>
    <div class="listing__photos listing__photos--wide" role="img" aria-label="Horses grazing below alpine mountains and a lakeside pod">
      <span class="tile t-horse"></span><span class="tile t-mount"></span><span class="tile t-lake"></span><span class="tile t-plain"></span>
      <span class="tile-tag tile-tag--right">5 suites<br>3 pods</span>
    </div>
    <p class="listing__body">A portfolio of destinations across New Zealand, each with striking scenery, luxury villas, a winery estate and an incredible restaurant.</p>
    <footer class="listing__foot"><span>www.kestrelgroup.com</span><span class="listing__brand">The Kestrel Group</span></footer>
  </article>

  <article class="listing">
    <p class="listing__label"><b>Stonevale Lodge, Craigieburn Valley,<br>South Island</b></p>
    <h3 class="listing__headline">A journey, an inspiration, a reprieve from the ordinary.</h3>
    <div class="listing__photos listing__photos--wide" role="img" aria-label="Snowy peaks above a valley station and lodge interior">
      <span class="tile t-mount"></span><span class="tile t-hill"></span><span class="tile t-plain"></span><span class="tile t-lake"></span>
    </div>
    <p class="listing__body">Villa-style suites open to the valley’s rolling vineyards, with a revitalised dining scene, wine cellar and speakeasy bar.</p>
    <footer class="listing__foot"><span>www.stonevale.com</span><span class="listing__brand"><i></i>Stonevale</span></footer>
  </article>
</section>

<!-- Front, plain -->
<section class="sheet sheet--front-plain">
  <aside class="identity">
    <div class="identity__mark"><i></i>Veridane</div>
    <div class="identity__title">
      <h2 class="tagline">Experiential<br>Luxury</h2>
      <div class="portfolio">The<br>Veridane<br>portfolio<ul><li>Australia</li><li>New Zealand</li><li>Chile</li><li>Canada</li></ul></div>
    </div>
    <address class="contact"><div class="contact__name">Marla Quinn</div>Marla@Veridane.net<br><span class="contact__phone">555-210-4478</span><br>www.veridane.net</address>
  </aside>

  <article class="listing">
    <p class="listing__label"><b>Coralis</b><br><span>Hamilton Island, Queensland</span></p>
    <h3 class="listing__headline">Exquisite Great Barrier Reef experience</h3>
    <div class="listing__photos" role="img" aria-label="Island resort, heart-shaped reef from above and seafood platter">
      <span class="tile t-dusk"></span><span class="tile tile--tall t-food"></span><span class="tile t-reef"></span>
      <span class="tile-tag tile-tag--low">16+ years<br>60 Pavilions</span>
    </div>
    <p class="listing__body">Unsurpassed beauty, privacy and intuitive service. Stay three nights to explore Hamilton Island and the Great Barrier Reef.</p>
    <footer class="listing__foot"><span>www.coralis.com.au</span><span class="listing__brand">Coralis</span></footer>
  </article>

  <article class="listing">
    <p class="listing__label"><b>Chile: Vientos Hotels:<br>Atacama, Chiloé &amp; Patagonia</b></p>
    <p class="listing__group">Harrow Lodges</p>
    <h3 class="listing__headline">Family run and welcoming to children 10+ years</h3>
    <div class="listing__photos listing__photos--wide" role="img" aria-label="Desert lodge with horses, lake boat and mountain views">
      <span class="tile t-plain" style="grid-column:span 2"></span><span class="tile t-lake"></span><span class="tile t-river"></span>
      <span class="tile-tag tile-tag--top">10+ years<br>28-40 Suites</span>
    </div>
    <p class="listing__body">Vientos Hotels are a collection of small boutique hotels across Chile, each with a tangible energy and a true connection to place.</p>
    <footer class="listing__foot"><span>info@vientoshotels.com</span><span class="listing__brand"><i></i>Vientos</span></footer>
  </article>

  <article class="listing">
    <p class="listing__label"><b>Canada: Cedarline Wilderness Lodge,<br>Vancouver Island, British Columbia</b><br><span>Harrow Lodges</span></p>
    <h3 class="listing__headline">A true Canadian Safari experience</h3>
    <div class="listing__photos" role="img" aria-label="Riders crossing a river, forest canopy tents and wildlife">
      <span class="tile t-mount"></span><span class="tile t-river"></span><span class="tile t-forest"></span><span class="tile t-hill"></span>
      <span class="tile-tag tile-tag--top">6+ years<br>25 Tents</span>
    </div>
    <p class="listing__body">Cedarline Wilderness Lodge, set in remote Vancouver Island, delivers wild luxury under canvas.</p>
    <footer class="listing__foot"><span>www.cedarlinewilderness.com</span><span class="listing__brand">Cedarline</span></footer>
  </article>

  <article class="listing">
    <p class="listing__label"><b>New Zealand<br>Taurapa Lodge, Taupo, North Island</b><br><span>Harrow Lodges</span></p>
    <h3 class="listing__headline">New Zealand’s fly-fishing premium lodges</h3>
    <div class="listing__photos listing__photos--wide" role="img" aria-label="Stone lodge on manicured lawn beside a river">
      <span class="tile t-stone"></span><span class="tile t-river"></span><span class="tile t-hill"></span><span class="tile t-forest"></span>
      <span class="tile-tag tile-tag--right">22 Suites/<br>Residences</span>
    </div>
    <p class="listing__body">Taurapa Lodge delivers warm hospitality and views of the Waikato River. Fly fishing, rafting, golf, spa and heli excursions. A 3 night stay is ideal.</p>
    <footer class="listing__foot"><span>www.taurapalodge.com</span><span class="listing__brand">Taurapa Lodge</span></footer>
  </article>

  <article class="listing">
    <p class="listing__label"><b>The Kestrel Group</b><br><span>North &amp; South Islands</span></p>
    <h3 class="listing__headline">Artistic architecture to complement the environments</h3>
    <div class="listing__photos listing__photos--wide" role="img" aria-label="Horses grazing below alpine mountains and a lakeside pod">
      <span class="tile t-horse"></span><span class="tile t-mount"></span><span class="tile t-lake"></span><span class="tile t-plain"></span>
      <span class="tile-tag tile-tag--right">5 suites<br>3 pods</span>
    </div>
    <p class="listing__body">A portfolio of destinations across New Zealand, each with striking scenery, luxury villas, a winery estate and an incredible restaurant.</p>
    <footer class="listing__foot"><span>www.kestrelgroup.com</span><span class="listing__brand">The Kestrel Group</span></footer>
  </article>

  <article class="listing">
    <p class="listing__label"><b>Stonevale Lodge, Craigieburn Valley,<br>South Island</b></p>
    <h3 class="listing__headline">A journey, an inspiration, a reprieve from the ordinary.</h3>
    <div class="listing__photos listing__photos--wide" role="img" aria-label="Snowy peaks above a valley station and lodge interior">
      <span class="tile t-mount"></span><span class="tile t-hill"></span><span class="tile t-plain"></span><span class="tile t-lake"></span>
    </div>
    <p class="listing__body">Villa-style suites open to the valley’s rolling vineyards, with a revitalised dining scene, wine cellar and speakeasy bar.</p>
    <footer class="listing__foot"><span>www.stonevale.com</span><span class="listing__brand"><i></i>Stonevale</span></footer>
  </article>
</section>

<!-- Back, tinted -->
<section class="sheet sheet--back-tinted">
  <aside class="identity">
    <div class="identity__mark"><i></i>Veridane</div>
    <div class="identity__title">
      <h2 class="tagline">Experiential<br>Luxury</h2>
      <div class="portfolio">The<br>Veridane<br>portfolio<ul><li>Australia</li><li>New Zealand</li><li>Chile</li><li>Canada</li></ul></div>
    </div>
    <address class="contact"><div class="contact__name">Marla Quinn</div>Marla@Veridane.net<br><span class="contact__phone">555-210-4478</span><br>www.veridane.net</address>
  </aside>

  <article class="listing listing--aqua">
    <p class="listing__label"><b>Wild Estates of Australia</b></p>
    <h3 class="listing__headline listing__headline--teal" style="margin-top:10px">Independently owned and operated luxury lodges</h3>
    <div class="listing__photos" role="img" aria-label="White sand beach, coastal bush and lakeside lodge">
      <span class="tile t-beach"></span><span class="tile tile--tall t-forest"></span><span class="tile t-plain"></span>
    </div>
    <p class="listing__body">Each lodge has signature experiences showcasing the natural landscapes and wildlife of its region, both land and marine.</p>
    <footer class="listing__foot"><span>www.wildestatesofaustralia.com.au</span><span class="listing__brand"><i></i>Wild Estates</span></footer>
  </article>

  <article class="listing">
    <p class="listing__label"><b>Marrin Lodge</b><br><span>Lord Howe Island, New South Wales</span></p>
    <p class="listing__group">Harrow Lodges</p>
    <h3 class="listing__headline">A top romantic Lovers Bay</h3>
    <div class="listing__photos" role="img" aria-label="Island peaks, lagoon, fresh salad and fish dish">
      <span class="tile t-hill"></span><span class="tile t-food"></span><span class="tile t-sea"></span><span class="tile t-night"></span>
    </div>
    <p class="listing__body">Celebrated as the pinnacle of luxury on World Heritage-listed Lord Howe Island, with island-inspired dining and a barefoot vibe.</p>
    <footer class="listing__foot"><span>www.marrinlodge.com.au</span><span class="listing__brand">Marrin</span></footer>
  </article>

  <article class="listing listing--rose">
    <p class="listing__label"><b>Meridian 29</b><br><span>Uluru-Kata Tjuta, Northern Territory</span></p>
    <p class="listing__group">Harrow Lodges</p>
    <h3 class="listing__headline listing__headline--maroon">Australia’s best-known natural icon</h3>
    <div class="listing__photos" role="img" aria-label="Outdoor dinner under red sky, tented pavilion and plunge pool">
      <span class="tile t-red"></span><span class="tile tile--tall t-sunset"></span><span class="tile t-night"></span>
    </div>
    <p class="listing__body">Luxury tented pavilions with views of Uluru. Red Centre experiences, local cuisine and world-class service.</p>
    <footer class="listing__foot"><span>www.meridian29.com.au</span><span class="listing__brand">Meridian 29</span></footer>
  </article>

  <article class="listing">
    <p class="listing__label"><b>Fernhollow Lodge</b><br><span>Daintree Rainforest, Queensland</span></p>
    <p class="listing__group">Harrow Lodges</p>
    <h3 class="listing__headline">Tropical North Queensland’s luxury basecamp</h3>
    <div class="listing__photos listing__photos--wide" role="img" aria-label="Rainforest treehouse, lounge bar and pool">
      <span class="tile t-forest"></span><span class="tile t-room"></span><span class="tile t-pool"></span><span class="tile t-hill"></span>
    </div>
    <p class="listing__body">Set for access to the region’s natural attractions, with views over the river and forty private treehouses.</p>
    <footer class="listing__foot"><span>www.fernhollowlodge.com.au</span><span class="listing__brand">Fernhollow</span></footer>
  </article>

  <article class="listing listing--slate">
    <p class="listing__label"><b>Cliffward Lodge</b><br><span>Kangaroo Island, South Australia</span></p>
    <p class="listing__group">Harrow Lodges</p>
    <h3 class="listing__headline">Australia’s third largest island</h3>
    <div class="listing__photos listing__photos--wide" role="img" aria-label="Clifftop lounge with fireplace, coastline and plated dish">
      <span class="tile tile--tall t-room"></span><span class="tile t-sea"></span><span class="tile t-food"></span>
    </div>
    <p class="listing__body">Perched on a clifftop above the bay, with a new spa, fitness centre and a four-bedroom ocean pavilion.</p>
    <footer class="listing__foot"><span>www.cliffwardlodge.com.au</span><span class="listing__brand">Cliffward</span></footer>
  </article>

  <article class="listing">
    <p class="listing__label"><b>The Amberlee</b><br><span>Barossa Valley, South Australia</span></p>
    <p class="listing__group">Harrow Lodges</p>
    <h3 class="listing__headline">An idyllic luxury vineyard retreat</h3>
    <div class="listing__photos listing__photos--wide" role="img" aria-label="Rolling vineyard rows, cellar and dining room">
      <span class="tile t-vine"></span><span class="tile t-plain"></span><span class="tile t-vine"></span><span class="tile t-room"></span>
    </div>
    <p class="listing__body">Villa-style suites open to the valley’s rolling vineyards, with a revitalised dining scene and wine cellar.</p>
    <footer class="listing__foot"><span>www.theamberlee.com.au</span><span class="listing__brand">The Amberlee</span></footer>
  </article>
</section>

<!-- Back, plain -->
<section class="sheet sheet--back-plain">
  <aside class="identity">
    <div class="identity__mark"><i></i>Veridane</div>
    <div class="identity__title identity__title--large">
      <h2 class="tagline">Experiential<br>Luxury</h2>
      <div class="portfolio">The<br>Veridane<br>portfolio<ul><li>Australia</li><li>New Zealand</li><li>Chile</li><li>Canada</li></ul></div>
    </div>
    <address class="contact"><div class="contact__name">Marla Quinn</div>Marla@Veridane.net<br><span class="contact__phone">555-210-4478</span><br>www.veridane.net</address>
  </aside>

  <article class="listing">
    <p class="listing__label"><b>Wild Estates of Australia</b></p>
    <h3 class="listing__headline listing__headline--teal" style="margin-top:10px">Independently owned and operated luxury lodges</h3>
    <div class="listing__photos" role="img" aria-label="White sand beach, coastal bush and lakeside lodge">
      <span class="tile t-beach"></span><span class="tile tile--tall t-forest"></span><span class="tile t-plain"></span>
    </div>
    <p class="listing__body">Each lodge has signature experiences showcasing the natural landscapes and wildlife of its region, both land and marine.</p>
    <footer class="listing__foot"><span>www.wildestatesofaustralia.com.au</span><span class="listing__brand"><i></i>Wild Estates</span></footer>
  </article>

  <article class="listing">
    <p class="listing__label"><b>Marrin Lodge</b><br><span>Lord Howe Island, New South Wales</span></p>
    <p class="listing__group">Harrow Lodges</p>
    <h3 class="listing__headline">A top romantic Lovers Bay</h3>
    <div class="listing__photos" role="img" aria-label="Island peaks, lagoon, fresh salad and fish dish">
      <span class="tile t-hill"></span><span class="tile t-food"></span><span class="tile t-sea"></span><span class="tile t-night"></span>
    </div>
    <p class="listing__body">Celebrated as the pinnacle of luxury on World Heritage-listed Lord Howe Island, with island-inspired dining and a barefoot vibe.</p>
    <footer class="listing__foot"><span>www.marrinlodge.com.au</span><span class="listing__brand">Marrin</span></footer>
  </article>

  <article class="listing">
    <p class="listing__label"><b>Meridian 29</b><br><span>Uluru-Kata Tjuta, Northern Territory</span></p>
    <p class="listing__group">Harrow Lodges</p>
    <h3 class="listing__headline listing__headline--maroon">Australia’s best-known natural icon</h3>
    <div class="listing__photos" role="img" aria-label="Outdoor dinner under red sky, tented pavilion and plunge pool">
      <span class="tile t-red"></span><span class="tile tile--tall t-sunset"></span><span class="tile t-night"></span>
    </div>
    <p class="listing__body">Luxury tented pavilions with views of Uluru. Red Centre experiences, local cuisine and world-class service.</p>
    <footer class="listing__foot"><span>www.meridian29.com.au</span><span class="listing__brand">Meridian 29</span></footer>
  </article>

  <article class="listing">
    <p class="listing__label"><b>Fernhollow Lodge</b><br><span>Daintree Rainforest, Queensland</span></p>
    <p class="listing__group">Harrow Lodges</p>
    <h3 class="listing__headline">Tropical North Queensland’s luxury basecamp</h3>
    <div class="listing__photos listing__photos--wide" role="img" aria-label="Rainforest treehouse, lounge bar and pool">
      <span class="tile t-forest"></span><span class="tile t-room"></span><span class="tile t-pool"></span><span class="tile t-hill"></span>
    </div>
    <p class="listing__body">Set for access to the region’s natural attractions, with views over the river and forty private treehouses.</p>
    <footer class="listing__foot"><span>www.fernhollowlodge.com.au</span><span class="listing__brand">Fernhollow</span></footer>
  </article>

  <article class="listing">
    <p class="listing__label"><b>Cliffward Lodge</b><br><span>Kangaroo Island, South Australia</span></p>
    <p class="listing__group">Harrow Lodges</p>
    <h3 class="listing__headline">Australia’s third largest island</h3>
    <div class="listing__photos listing__photos--wide" role="img" aria-label="Clifftop lounge with fireplace, coastline and plated dish">
      <span class="tile tile--tall t-room"></span><span class="tile t-sea"></span><span class="tile t-food"></span>
    </div>
    <p class="listing__body">Perched on a clifftop above the bay, with a new spa, fitness centre and a four-bedroom ocean pavilion.</p>
    <footer class="listing__foot"><span>www.cliffwardlodge.com.au</span><span class="listing__brand">Cliffward</span></footer>
  </article>

  <article class="listing">
    <p class="listing__label"><b>The Amberlee</b><br><span>Barossa Valley, South Australia</span></p>
    <p class="listing__group">Harrow Lodges</p>
    <h3 class="listing__headline">An idyllic luxury vineyard retreat</h3>
    <div class="listing__photos listing__photos--wide" role="img" aria-label="Rolling vineyard rows, cellar and dining room">
      <span class="tile t-vine"></span><span class="tile t-plain"></span><span class="tile t-vine"></span><span class="tile t-room"></span>
    </div>
    <p class="listing__body">Villa-style suites open to the valley’s rolling vineyards, with a revitalised dining scene and wine cellar.</p>
    <footer class="listing__foot"><span>www.theamberlee.com.au</span><span class="listing__brand">The Amberlee</span></footer>
  </article>
</section>

</body>
</html>
```